Political sign design, fonts colors and layout

I am running for Town Council.

My message is done, and *a draft is attached* with the text we wish to use. It says "Elect Dana Velloway" etc. In Maroon and White. I am not a designer, but this is somewhat close to what we are looking for.

I need help with colors and fonts, layout, spacing, and general cleanup.

I'm attaching the town high school logo:

- "B" for Brockmere: with black and white outlines on the fonts
- we want to incorporate the black and white on the fonts
- for the entire text, parts of the text, or best would be a mix

This is for signs printed and placed all over my town.

We need two versions

1. square, 4' by 4' version
2. 36" by 24" version

The smaller version will drop the three bullet pointed text, but otherwise can be identical.

The sign can only use 3 printed colors (due to printing costs.)

1. maroon,
2. white,
3. black.

The maroon should match the maroon from the high school logo attached, which I believe I did in the draft.

We also like the white border around the outside, like in the "scoreboard" design attached.

Thanks for your attention, wish me luck.

Dana

Target Market(s)

SIgns, Political market

Industry/Entity Type

Political

Font styles to use
Sans Serif
Other font styles liked:
• Arial Black, Sans Serif Bold

Requirements
Must have
• maroon background, white font.
• - black borders around fonts where appropriate
• - great spacing
• - great typeface usage
• - clean and crisp political sign, visible while driving.
• - my name "Dana Velloway" much larger like the draft, or the appropriate additional size
• - two versions, one square, and one 36" / 24"
Nice to have
• - nice borders
• - dress it up a bit, using italics and bold fonts, without making it flashy or busy.
Should not have
• Must be easily readable from a car, except for "Paid for by Friends of Dana Velloway" which can be tiny.
• Colors are noted in the description, the "Brockmere Maroon" as the background, white font, and some use of black.

```html
<!DOCTYPE html>
<html lang="en">
<head>
<meta charset="utf-8">
<title>Elect Dana Velloway – Yard Signs</title>
<link rel="stylesheet" href="https://fonts.googleapis.com/css2?family=Bebas+Neue&family=Montserrat:ital,wght@0,600;0,700;0,800;1,500&display=swap">
<style>
  :root {
    --maroon: #771b2e;
    --black: #050505;
    --white: #ffffff;
    --page: #ffffff;
    --display: "Bebas Neue", "Arial Narrow", sans-serif;
    --body: "Montserrat", Arial, sans-serif;
  }
  * { box-sizing: border-box; margin: 0; padding: 0; }
  html, body { width: 1200px; height: 480px; overflow: hidden; background: var(--page); }
  .canvas { position: relative; width: 1200px; height: 480px; }

  .sign { position: absolute; background: var(--maroon); color: var(--white); overflow: hidden; }
  .sign--square { left: 32px; top: 18px; width: 461px; height: 448px; }
  .sign--wide { left: 554px; top: 44px; width: 576px; height: 384px; }

  .headline-band {
    position: absolute; left: 0; right: 0; background: var(--black);
    font-family: var(--display); font-size: 46px; line-height: 1;
    display: flex; align-items: center; justify-content: center; padding-top: 4px;
  }
  .sign--square .headline-band { top: 25px; height: 54px; }
  .sign--wide .headline-band { top: 20px; height: 46px; font-size: 42px; }

  .candidate { position: absolute; display: flex; flex-direction: column; align-items: flex-end; }
  .sign--square .candidate { left: 78px; top: 114px; }
  .sign--wide .candidate { left: 114px; top: 96px; }
  .candidate__elect {
    align-self: flex-start; font-family: var(--display); font-size: 30px; line-height: .8;
  }
  .candidate__name {
    font-family: var(--display); font-size: 68px; line-height: .85; letter-spacing: .5px; white-space: nowrap;
  }
  .sign--wide .candidate__name { font-size: 74px; }
  .candidate__office {
    background: var(--black); font-family: var(--display); font-size: 14px;
    padding: 3px 4px 1px; line-height: 1; margin-top: 4px; letter-spacing: .2px;
  }

  .tagline, .website {
    position: absolute; left: 0; right: 0; text-align: center;
    font-family: var(--body); font-weight: 700;
  }
  .sign--square .tagline { top: 248px; font-size: 17px; }
  .sign--square .website { top: 287px; font-size: 18px; }
  .sign--wide .tagline { top: 222px; font-size: 20px; }
  .sign--wide .website { top: 248px; font-size: 20px; }

  .platform { position: absolute; list-style: none; font-family: var(--body); font-weight: 700; line-height: 1.25; }
  .sign--square .platform { left: 122px; top: 320px; font-size: 14px; }
  .sign--wide .platform { left: 322px; top: 308px; font-size: 13px; }
  .platform__emphasis { background: var(--black); padding: 0 3px; font-weight: 800; }

  .vote-band {
    position: absolute; background: var(--black); font-family: var(--display);
    display: flex; align-items: center; justify-content: center; gap: 8px; line-height: 1; padding-top: 5px;
  }
  .sign--square .vote-band { left: 0; right: 0; top: 380px; height: 46px; }
  .sign--wide .vote-band { left: 0; top: 302px; width: 316px; height: 58px; }
  .vote-band__date { font-size: 36px; }
  .vote-band__row { font-size: 54px; }

  .disclaimer { position: absolute; font-family: var(--body); font-style: italic; font-weight: 500; font-size: 7px; }
  .sign--square .disclaimer { left: 0; right: 0; bottom: 6px; text-align: center; }
  .sign--wide .disclaimer { left: 4px; top: 368px; }
</style>
</head>
<body>
<main class="canvas">

  <section class="sign sign--square" aria-label="Square sign, 4 by 4 feet">
    <h2 class="headline-band">Take Back Our Town</h2>
    <div class="candidate">
      <span class="candidate__elect">Elect</span>
      <h1 class="candidate__name">Dana Velloway</h1>
      <span class="candidate__office">For Brockmere Councilman/Trustee</span>
    </div>
    <p class="tagline">Fighting for Brockmere</p>
    <p class="website">www.votevelloway.com</p>
    <ul class="platform">
      <li>- Stop <span class="platform__emphasis">HIGH</span> taxes</li>
      <li>-Clean up our government</li>
      <li>-Preserve our Neighborhoods</li>
    </ul>
    <p class="vote-band"><span class="vote-band__date">Vote Nov. 8th</span><span class="vote-band__row">“Row A”</span></p>
    <p class="disclaimer">Paid for by Friends of Dana</p>
  </section>

  <section class="sign sign--wide" aria-label="Wide sign, 36 by 24 inches">
    <h2 class="headline-band">Take Back Our Town</h2>
    <div class="candidate">
      <span class="candidate__elect">Elect</span>
      <h1 class="candidate__name">Dana Velloway</h1>
      <span class="candidate__office">For Brockmere Councilman/Trustee</span>
    </div>
    <p class="tagline">Fighting for Brockmere</p>
    <p class="website">www.votevelloway.com</p>
    <p class="vote-band"><span class="vote-band__date">Vote Nov. 8th</span><span class="vote-band__row">“Row A”</span></p>
    <ul class="platform">
      <li>- Stop <span class="platform__emphasis">HIGH</span> taxes</li>
      <li>-Clean up our government</li>
      <li>-Preserve our Neighborhoods</li>
    </ul>
    <p class="disclaimer">Paid for by Friends of Dana</p>
  </section>

</main>
</body>
</html>
```